7Brink Plumbing flyer

I want to incorporate our logo design into a new flyer promoting the business and advertising products that we install.
We install hot water systems, Air-conditioning systems and central heating systems. Along with other aspects of plumbing such as gasfitting, roofing, sanitary and drainage
I would like the background to be the same as our business cards with the water effect and colours.

Requirements
Must have
• Logo
24/7 Emergency call out
Aspects of plumbing we do
- Hot water systems
- Central Heating
- Solar hot water systems/ heat pump systems
- Gasfitting
- Drainage
- Roofing
- Air-Conditioning
Nice to have
• Pictures of hot water systems and air-conditioning system
$30 off voucher when producing this flyer (limit 1 per house hold)

```html
<!DOCTYPE html>
<html lang="en">
<head>
<meta charset="utf-8">
<title>7Brink Plumbing Flyer</title>
<link rel="stylesheet" href="https://fonts.googleapis.com/css2?family=Lato:wght@400;700;900&family=Montserrat:wght@800&display=swap">
<style>
  :root {
    --stage: #707072;
    --charcoal: #38393b;
    --brand-blue: #1a8ad4;
    --pill-blue: #0e5789;
    --sky: #a9d8f3;
    --voucher-grey: #dcdcde;
    --white: #ffffff;
    --ink: #2b2b2b;
  }
  * { box-sizing: border-box; margin: 0; padding: 0; }
  html, body { width: 1200px; height: 1200px; overflow: hidden; }
  body { background: var(--stage); font-family: "Lato", sans-serif; position: relative; }

  .flyer { position: absolute; width: 536px; height: 689px; overflow: hidden; background: var(--white); }
  .flyer--front { left: 53px; top: 236px; }
  .flyer--back { left: 624px; top: 238px; }
  .flyer > * { position: absolute; }
  .flyer .backdrop { left: 0; top: 0; width: 536px; height: 689px; }

  /* front */
  .brand { left: 0; width: 536px; top: 52px; display: flex; justify-content: center; align-items: center; gap: 10px; }
  .brand__dot { width: 30px; height: 30px; border-radius: 50%; background: var(--brand-blue); }
  .brand__name { font-family: "Lato", sans-serif; font-weight: 700; font-size: 30px; color: var(--white); line-height: 1; }
  .headline { left: 0; width: 536px; text-align: center; color: var(--white); font-family: "Montserrat", sans-serif; font-weight: 800; }
  .headline--big { top: 116px; font-size: 86px; line-height: 1; }
  .headline--sub { top: 198px; font-size: 29px; line-height: 1; }
  .product-shot { left: 34px; top: 282px; width: 470px; height: 246px; border-radius: 6px;
    background: linear-gradient(160deg, #f4f6f8 0%, #dfe4e9 60%, #c9cfd5 100%); opacity: .92; }

  /* voucher */
  .voucher { width: 318px; height: 94px; background: var(--voucher-grey); }
  .voucher__band { position: absolute; left: 0; top: 0; width: 100%; height: 52px; background: var(--brand-blue); }
  .voucher__perf { position: absolute; left: 16px; top: 6px; height: 82px; border-left: 2px dotted var(--white); }
  .voucher__badge { position: absolute; left: 26px; top: 1px; width: 92px; height: 92px; border-radius: 50%; background: var(--white); display: flex; align-items: center; justify-content: center; }
  .voucher__badge span { width: 80px; height: 80px; border-radius: 50%; background: var(--brand-blue); color: var(--white); font-weight: 900; font-size: 27px; line-height: .9; text-align: center; display: flex; align-items: center; justify-content: center; }
  .voucher__title { position: absolute; left: 135px; top: 10px; font-weight: 900; font-size: 31px; line-height: 1; color: var(--white); }
  .voucher__terms { position: absolute; left: 135px; top: 57px; font-size: 12.5px; line-height: 1.2; color: var(--ink); white-space: nowrap; }
  .flyer--front .voucher { left: 125px; top: 532px; }
  .flyer--back .voucher { left: 184px; top: 545px; }

  .footer-bar { left: 0; top: 644px; width: 536px; height: 45px; background: var(--brand-blue); color: var(--white); text-align: center; font-size: 12.5px; letter-spacing: 2.4px; line-height: 45px; }

  /* back */
  .hero-photo { left: 0; top: 0; width: 536px; height: 370px;
    background: linear-gradient(120deg, #e9ecef 0%, #b9c1c8 45%, #8f979e 100%); }
  .section-title { left: 101px; top: 299px; width: 360px; height: 56px; border-radius: 22px 22px 0 0; background: var(--pill-blue); color: var(--white); font-weight: 900; font-size: 19.5px; text-align: center; padding-top: 15px; }
  .service-list { list-style: none; color: var(--white); font-size: 15.5px; line-height: 1.05; }
  .service-list li { display: flex; align-items: flex-start; gap: 7px; }
  .service-list svg { flex: none; width: 15px; height: 15px; margin-top: 1px; }
  .service-list--left { left: 72px; top: 392px; width: 210px; }
  .service-list--left li { margin-bottom: 14px; }
  .service-list--right { left: 312px; top: 391px; width: 200px; }
  .service-list--right li { margin-bottom: 8.5px; }
  .detail-photo { left: 27px; top: 513px; width: 118px; height: 118px; border-radius: 50%; border: 4px solid var(--white);
    background: radial-gradient(circle at 45% 40%, #f2f2f2 0%, #cfd3d6 70%, #aeb3b7 100%); }
  .contact-rule { left: 0; top: 655px; width: 536px; border-top: 1px solid rgba(255,255,255,.8); }
  .contact-line { left: 0; top: 660px; width: 536px; text-align: center; color: var(--white); font-size: 12.5px; word-spacing: 1px; white-space: nowrap; }
  .contact-line .sep { margin: 0 14px; }
</style>
</head>
<body>

<section class="flyer flyer--front">
  <svg class="backdrop" viewBox="0 0 536 689" aria-hidden="true">
    <defs>
      <linearGradient id="frontBlue" x1="0" y1="0" x2="0" y2="1">
        <stop offset="0" stop-color="#0f77c0"/>
        <stop offset="1" stop-color="#27a3e6"/>
      </linearGradient>
      <linearGradient id="frontDark" x1="0" y1="0" x2="0" y2="1">
        <stop offset="0" stop-color="#3c3d40"/>
        <stop offset="1" stop-color="#2e2f31"/>
      </linearGradient>
    </defs>
    <rect width="536" height="320" fill="url(#frontDark)"/>
    <path d="M0 208 Q268 351 536 222 L536 689 L0 689Z" fill="#fff"/>
    <path d="M0 217 Q268 360 536 231 L536 689 L0 689Z" fill="url(#frontBlue)"/>
    <path d="M0 498 Q300 408 536 386 L536 689 L0 689Z" fill="var(--sky)"/>
    <path d="M0 511 Q300 420 536 399 L536 689 L0 689Z" fill="#fff"/>
  </svg>

  <div class="brand">
    <span class="brand__dot"></span>
    <span class="brand__name">7Brink Plumbing</span>
  </div>
  <div class="headline headline--big">24/7</div>
  <div class="headline headline--sub">EMERGENCY CALL OUT</div>

  <div class="product-shot" role="img" aria-label="Hot water cylinder, split air-conditioning units and remote control"></div>

  <div class="voucher">
    <div class="voucher__band"></div>
    <div class="voucher__perf"></div>
    <div class="voucher__badge"><span>$30<br>OFF</span></div>
    <div class="voucher__title">VOUCHER</div>
    <div class="voucher__terms">when producing this flyer<br>(limit 1 per house hold)</div>
  </div>

  <div class="footer-bar">www.7brinkplumbing.com</div>
</section>

<section class="flyer flyer--back">
  <div class="hero-photo" role="img" aria-label="Plumber in cap and overalls adjusting the controls of a hot water cylinder"></div>

  <div class="section-title">ASPECTS OF PLUMBING WE DO</div>

  <svg class="backdrop" viewBox="0 0 536 689" aria-hidden="true">
    <defs>
      <linearGradient id="backBlue" gradientUnits="userSpaceOnUse" x1="0" y1="300" x2="0" y2="620">
        <stop offset="0" stop-color="#0f75bd"/>
        <stop offset="1" stop-color="#2ea6e8"/>
      </linearGradient>
    </defs>
    <path d="M0 297 Q268 425 536 306 L536 320 Q268 440 0 311Z" fill="#fff"/>
    <path d="M0 311 Q268 440 536 320 L536 689 L0 689Z" fill="url(#backBlue)"/>
    <path d="M0 586 Q268 492 536 498 L536 689 L0 689Z" fill="var(--sky)"/>
    <path d="M0 598 Q268 504 536 509 L536 689 L0 689Z" fill="var(--charcoal)"/>
  </svg>

  <ul class="service-list service-list--left">
    <li><svg viewBox="0 0 16 16"><circle cx="8" cy="8" r="7" fill="none" stroke="#fff" stroke-width="1.3"/><path d="M4.6 8.2l2.3 2.2 4.4-4.6" fill="none" stroke="#fff" stroke-width="1.5"/></svg>Hot water systems</li>
    <li><svg viewBox="0 0 16 16"><circle cx="8" cy="8" r="7" fill="none" stroke="#fff" stroke-width="1.3"/><path d="M4.6 8.2l2.3 2.2 4.4-4.6" fill="none" stroke="#fff" stroke-width="1.5"/></svg>Central Heating</li>
    <li><svg viewBox="0 0 16 16"><circle cx="8" cy="8" r="7" fill="none" stroke="#fff" stroke-width="1.3"/><path d="M4.6 8.2l2.3 2.2 4.4-4.6" fill="none" stroke="#fff" stroke-width="1.5"/></svg>Solar hot water systems/<br>heat pump systems</li>
  </ul>
  <ul class="service-list service-list--right">
    <li><svg viewBox="0 0 16 16"><circle cx="8" cy="8" r="7" fill="none" stroke="#fff" stroke-width="1.3"/><path d="M4.6 8.2l2.3 2.2 4.4-4.6" fill="none" stroke="#fff" stroke-width="1.5"/></svg>Gasfitting</li>
    <li><svg viewBox="0 0 16 16"><circle cx="8" cy="8" r="7" fill="none" stroke="#fff" stroke-width="1.3"/><path d="M4.6 8.2l2.3 2.2 4.4-4.6" fill="none" stroke="#fff" stroke-width="1.5"/></svg>Drainage</li>
    <li><svg viewBox="0 0 16 16"><circle cx="8" cy="8" r="7" fill="none" stroke="#fff" stroke-width="1.3"/><path d="M4.6 8.2l2.3 2.2 4.4-4.6" fill="none" stroke="#fff" stroke-width="1.5"/></svg>Roofing</li>
    <li><svg viewBox="0 0 16 16"><circle cx="8" cy="8" r="7" fill="none" stroke="#fff" stroke-width="1.3"/><path d="M4.6 8.2l2.3 2.2 4.4-4.6" fill="none" stroke="#fff" stroke-width="1.5"/></svg>Air-Conditioning</li>
  </ul>

  <div class="detail-photo" role="img" aria-label="Hand turning the dial of an electric water heater"></div>

  <div class="voucher">
    <div class="voucher__band"></div>
    <div class="voucher__perf"></div>
    <div class="voucher__badge"><span>$30<br>OFF</span></div>
    <div class="voucher__title">VOUCHER</div>
    <div class="voucher__terms">when producing this flyer<br>(limit 1 per house hold)</div>
  </div>

  <div class="contact-rule"></div>
  <div class="contact-line">0400 555 218<span class="sep">|</span>hello@7brinkplumbing.com<span class="sep">|</span>www.7brinkplumbing.com</div>
</section>

</body>
</html>
```